Label design for one hand cream.

The name of the company is Luvo. We are launching a hand cream that is also an immediate cleaner without any water. It removes dirt from your hands without using water. After the use, your hands will be soft. It could be used in your feet too.

The company logo reminds of plants, nature and we would like this approach too. Please, remove the words "Produtos Naturais" from the logo.

Target Market(s)

Public in General. Mostly women.

Industry/Entity Type

Cosmetics

Font styles to use
Sans Serif

Colors
33b8a4
00a990
9bcb3c
acd036
fee087
fece3e
ffc214
fbed22
fbee3e

Requirements
Must have
• You must use the words in the label. Please, see the file attached but just use the WORDS, not the same structure. The image must be 15,5cm high and 7,5 cm wide.
• Use a darker green and some GOLDEN lines or details. You can even put the Logo plant on the golden color.
• "Frisson Duo"
• "Ação 3 em 1: Esfoliante, limpeza e hidratação"
• "Regeneração Celular"
• "Velvet Tending"
• Logo of the company "Luvo" (attached).
• Please, REMOVE the words "Produtos Naturais" from the logo.
• Elegance and show softness.
• Something that reminds of nature or fresh.
Should not have
• Strong colors or many images that distract the information.

```html
<!DOCTYPE html>
<html lang="pt">
<head>
<meta charset="UTF-8">
<title>Luvo – Frisson Duo label</title>
<link href="https://fonts.googleapis.com/css2?family=Oswald:wght@600;700&family=Encode+Sans+Condensed:wght@400;700&display=swap" rel="stylesheet">
<style>
  :root {
    --stage: #ecebe8;
    --paper: #ffffff;
    --green-dark: #0f7a3a;
    --green: #16873f;
    --gold-light: #fbe37a;
    --gold: #f3c53a;
    --gold-deep: #d89b1c;
    --cream: #f1e6c4;
    --ink: #1b1b1b;
  }
  * { margin: 0; padding: 0; box-sizing: border-box; }
  html, body { width: 1200px; height: 897px; overflow: hidden; background: var(--stage); }
  .stage { position: relative; width: 1200px; height: 897px; }
  .label {
    position: absolute; left: 382px; top: 0;
    width: 436px; height: 897px;
    background: var(--paper); overflow: hidden;
  }
  .label svg.shapes { position: absolute; inset: 0; }
  .brand {
    position: absolute; left: 58px; top: 52px;
    display: flex; align-items: center; gap: 14px;
    font-family: "Encode Sans Condensed", sans-serif; font-weight: 700;
    font-size: 92px; line-height: 1; color: var(--green);
  }
  .brand-dot { width: 34px; height: 34px; border-radius: 50%; background: var(--green); }
  .product {
    position: absolute; left: 0; width: 436px; top: 286px; text-align: center;
    font-family: "Oswald", sans-serif; font-weight: 700; color: var(--green);
    font-size: 70px; line-height: 0.98; letter-spacing: -0.5px;
  }
  .claim {
    position: absolute; left: 0; width: 436px; top: 436px; text-align: center;
    font-family: "Encode Sans Condensed", sans-serif; font-weight: 400;
    font-size: 21px; line-height: 1.2; color: var(--ink);
  }
  .benefits {
    position: absolute; left: 32px; top: 562px;
    font-family: "Encode Sans Condensed", sans-serif; font-weight: 700;
    font-size: 30px; line-height: 1.3; color: var(--green);
  }
  .weight {
    position: absolute; left: 0; top: 806px; width: 98px; height: 40px;
    background: var(--green); color: #fff;
    font-family: "Oswald", sans-serif; font-weight: 600; font-size: 22px;
    display: flex; align-items: center; justify-content: center;
  }
</style>
</head>
<body>
<main class="stage">
  <section class="label">
    <svg class="shapes" width="436" height="897" viewBox="0 0 436 897">
      <defs>
        <linearGradient id="ribbonFill" x1="0" y1="0" x2="1" y2="0">
          <stop offset="0" stop-color="#f6f1e0"/>
          <stop offset="1" stop-color="#fbf8ee"/>
        </linearGradient>
        <linearGradient id="bandFill" x1="0" y1="0" x2="1" y2="0.3">
          <stop offset="0" stop-color="var(--gold-deep)"/>
          <stop offset="0.35" stop-color="var(--gold-light)"/>
          <stop offset="0.7" stop-color="var(--gold)"/>
          <stop offset="1" stop-color="var(--gold-deep)"/>
        </linearGradient>
        <linearGradient id="leafFill" x1="0" y1="0" x2="1" y2="1">
          <stop offset="0" stop-color="#f7d86a"/>
          <stop offset="1" stop-color="#c8901c"/>
        </linearGradient>
      </defs>
      <path role="img" aria-label="Soft cream ribbon lines sweeping down the label"
            d="M40 0 C140 260 150 600 300 897 L200 897 C60 620 60 260 0 40 Z" fill="url(#ribbonFill)"/>
      <path d="M0 296 C140 268 290 200 436 172 L436 448 C320 470 260 520 200 516 C120 512 60 470 0 456 Z"
            fill="url(#bandFill)"/>
      <path d="M0 456 C60 470 120 512 200 516 C260 520 320 470 436 448"
            fill="none" stroke="var(--green)" stroke-width="3"/>
      <path d="M0 296 C140 268 290 200 436 172" fill="none" stroke="var(--green)" stroke-width="2"/>
      <path role="img" aria-label="Golden leaf illustration rising from the lower corner"
            d="M230 897 C260 760 320 660 420 600 L436 600 L436 897 Z" fill="url(#leafFill)"/>
    </svg>

    <div class="brand"><span class="brand-dot"></span>Luvo</div>
    <h1 class="product">FRISSON<br>DUO</h1>
    <p class="claim">Ação 3 em 1: Esfoliante,<br>limpeza e hidratação</p>
    <p class="benefits">Regeneração Celular<br>Velvet Tending</p>
    <div class="weight">195g</div>
  </section>
</main>
</body>
</html>
```